Etiketten für selbst erzeugten Obstbrand und Liköre
Zielgruppe
Freunde und Bekannte
Aufgabenstellung
Die Etiketten kommen auf Flaschen, die selbst erzeugten Obstbrand und Liköre enthalten. Das Etikett sollte modern, ohne Schnickschnack und edel aussehen. Das Etikett sollte nur aus grafischen Elementen und Schrift bestehen (keine Bilder/Fotos). Die Schnapssorte selbst trage ich auf einem reservierten Feld handschriftlich auf dem Etikett ein. Es sollte maximal 7cm hoch und 10cm breit sein. Die Flaschen werden ausschließlich verschenkt.

```html
<!DOCTYPE html>
<html lang="de">
<head>
<meta charset="utf-8">
<title>Mit Herz gemacht – Flaschenetikett</title>
<link rel="stylesheet" href="https://fonts.googleapis.com/css2?family=Varela+Round&display=swap">
<style>
  :root {
    --paper: #ffffff;
    --label: #000000;
    --ink: #ffffff;
  }
  html, body {
    margin: 0;
    padding: 0;
    width: 1200px;
    height: 840px;
    overflow: hidden;
    background: var(--paper);
  }
  .label-sheet {
    display: block;
    width: 1200px;
    height: 840px;
  }
  .label-disc { fill: var(--label); }
  .arc-title {
    font-family: "Varela Round", "Nunito", sans-serif;
    font-size: 40px;
    letter-spacing: 5px;
    fill: var(--ink);
  }
  .heart-mark { fill: var(--ink); }
  .field-line-name {
    stroke: var(--ink);
    stroke-width: 5;
    stroke-dasharray: 16 7;
  }
  .field-line-date {
    stroke: var(--ink);
    stroke-width: 3;
  }
</style>
</head>
<body>
<svg class="label-sheet" viewBox="0 0 1200 840" xmlns="http://www.w3.org/2000/svg">
  <defs>
    <path id="title-arc" d="M 376 413 A 215 215 0 0 1 806 413"/>
  </defs>

  <circle class="label-disc" cx="591" cy="413" r="277"/>

  <text class="arc-title" text-anchor="middle">
    <textPath href="#title-arc" startOffset="23.5%">MIT</textPath>
  </text>
  <text class="arc-title" text-anchor="middle">
    <textPath href="#title-arc" startOffset="65%">GEMACHT</textPath>
  </text>

  <g class="heart-mark" transform="translate(515 212) rotate(-20)">
    <path d="M 0 18 C -8 10 -26 0 -26 -10 C -26 -22 -10 -26 0 -14 C 10 -26 26 -22 26 -10 C 26 0 8 10 0 18 Z"/>
  </g>

  <line class="field-line-name" x1="381" y1="450" x2="801" y2="450"/>
  <line class="field-line-date" x1="487" y1="618" x2="694" y2="618"/>
</svg>
</body>
</html>
```